Lumo4Kart - a fintech company - business card

We need a business card design for our Payments Technology company in Sydney, Australia. We provide business with payment solutions expanding across EFTPOS machines, online payment gateways and mobile payment solutions. We would like to see designs that are clean, classy and professional.
Target Market(s)
Business professionals, executives, c-suite
Industry/Entity Type
Fintech
Contact Information for Business Card
Will be on 400gsm. Logo will most likely be spot gloss unless designer recommends otherwise.
Font styles to use
Sans Serif
Requirements
Must have
- We need our website (lumo4kart.com.au), email (contact@lumo4kart.com.au), mobile (0432 587 904) and direct phone number (02 6815 3927) to feature on the card along with our logo (attached) and the words "EFTPOS | ONLINE | MOBILE"
- Font = Roboto

```html
<!DOCTYPE html>
<html lang="en">
<head>
<meta charset="utf-8">
<title>Lumo4Kart Business Card</title>
<link href="https://fonts.googleapis.com/css2?family=Roboto:wght@400;500;700&display=swap" rel="stylesheet">
<style>
  :root {
    --brand-blue: #1d5f92;
    --ink-grey: #6b6b6b;
    --card-white: #ffffff;
    --backdrop: #e6e6e8;
    --font-main: "Roboto", Arial, sans-serif;
  }
  * { margin: 0; padding: 0; box-sizing: border-box; }
  html, body {
    width: 1200px; height: 900px; overflow: hidden;
    background: var(--backdrop);
    font-family: var(--font-main);
  }
  .sheet {
    width: 1200px; height: 900px;
    display: flex; flex-direction: column;
    align-items: center; justify-content: center; gap: 40px;
  }
  .card {
    position: relative;
    width: 700px; height: 400px;
    box-shadow: 0 6px 18px rgba(0,0,0,0.12);
  }
  /* Front */
  .card-front { background: var(--brand-blue); color: var(--card-white); }
  .front-brand {
    position: absolute; left: 0; right: 0; top: 130px;
    display: flex; align-items: center; justify-content: center; gap: 18px;
  }
  .front-brand-dot {
    width: 64px; height: 64px; border-radius: 50%; background: var(--card-white);
  }
  .front-brand-name {
    font-size: 56px; font-weight: 700; letter-spacing: 1px; color: var(--card-white);
  }
  .service-line {
    position: absolute; left: 0; right: 0; top: 268px;
    text-align: center; font-size: 19px; font-weight: 400; letter-spacing: 1.5px;
    word-spacing: 10px;
  }
  /* Back */
  .card-back { background: var(--card-white); }
  .back-brand {
    position: absolute; right: 44px; top: 52px;
    display: flex; align-items: center; gap: 14px;
  }
  .back-brand-dot { width: 52px; height: 52px; border-radius: 50%; background: var(--brand-blue); }
  .back-brand-name { font-size: 40px; font-weight: 700; color: var(--ink-grey); letter-spacing: 0.5px; }
  .rule-long {
    position: absolute; left: 300px; right: 40px; top: 214px;
    height: 2px; background: var(--brand-blue);
  }
  .person { position: absolute; left: 50px; top: 160px; }
  .person-name { font-size: 32px; font-weight: 700; color: var(--brand-blue); line-height: 1.1; }
  .person-role { font-size: 20px; color: var(--ink-grey); margin-top: 4px; }
  .rule-short {
    position: absolute; left: 50px; width: 240px; top: 258px;
    height: 2px; background: var(--brand-blue);
  }
  .contact-list {
    position: absolute; left: 60px; top: 276px;
    list-style: none; font-size: 17px; color: var(--ink-grey); line-height: 1.35;
  }
  .address {
    position: absolute; right: 44px; top: 232px;
    text-align: right; font-size: 16px; color: var(--ink-grey); line-height: 1.4;
    font-style: normal;
  }
  .website {
    position: absolute; left: 420px; top: 332px;
    font-size: 17px; color: var(--brand-blue);
  }
</style>
</head>
<body>
<main class="sheet">
  <section class="card card-front" aria-label="Card front">
    <div class="front-brand">
      <span class="front-brand-dot"></span>
      <span class="front-brand-name">Lumo4Kart</span>
    </div>
    <p class="service-line">EFTPOS | ONLINE | MOBILE</p>
  </section>

  <section class="card card-back" aria-label="Card back">
    <div class="back-brand">
      <span class="back-brand-dot"></span>
      <span class="back-brand-name">LUMO4KART</span>
    </div>
    <div class="rule-long"></div>
    <div class="person">
      <p class="person-name">Marten Vale</p>
      <p class="person-role">General Manager</p>
    </div>
    <div class="rule-short"></div>
    <ul class="contact-list">
      <li>02 6815 3927</li>
      <li>0432 587 904</li>
      <li>contact@lumo4kart.com.au</li>
    </ul>
    <address class="address">Harlow Crossing, Brenmoor<br>Westvale Park, 2041</address>
    <p class="website">lumo4kart.com.au</p>
  </section>
</main>
</body>
</html>
```